Packaging design for Organic Beard Care brand - Talon Meadows

This packaging design will be for our beard oil collection which include five different beard oil scents and our signature blend beard oil which is separate from the collection.
There will be two different variants of the box design needed:
Variant 1: White box with Logo and text (Ingredients, Directions, etc).
The words “Handcrafted Premium Beard Oil” will be printed in green foil color. Work this into the design.
Variant 2: Black box with gold foil logo and gold foil text (Ingredients, Directions, etc).
The words “Handcrafted Premium Beard Oil” will be printed in gold foil color. Work this into the design.
Both boxes should have a premium look and feel to it without too much noise.
(Think Brisk deodorant & shampoo brand or Plume teeth whitening brand)
Key callouts will be provided to add to the box designs.
I’ve attached icons, logos, images of the beard oil products and UPC codes that should be used on each box variant.
Please message me if there are more image assets or questions you have about creating the package design.
**Important** - You must create the design on the template file: 30ml-cardboard-box-template-talon-meadows.ai. Any submissions without the design within this template will be passed up/rejected.
Men 21-50
Health & Beauty Cosmetics
- Miso, ASAP Condensed

```html
<!DOCTYPE html>
<html lang="en">
<head>
<meta charset="utf-8">
<title>Talon Meadows – Premium Beard Oil Packaging</title>
<link rel="stylesheet" href="https://fonts.googleapis.com/css2?family=Asap+Condensed:wght@400;600;700&family=Raleway:wght@400;500;600&display=swap">
<style>
  :root{
    --backdrop:#bdbdbd;
    --white-side:#ffffff;
    --white-front:#f1f1f1;
    --white-front-low:#e2e2e2;
    --black-side:#1a1a1a;
    --black-front:#151515;
    --ink-dark:#2b2b2b;
    --ink-light:#f2f2f2;
    --foil-green:#1fb52c;
    --foil-green-deep:#0f8f1d;
    --foil-gold:#d9c07a;
    --foil-gold-deep:#a98a3e;
    --accent-orange:#ee8a2c;
    --badge-orange:#f0a465;
    --badge-grey:#9a9a9a;
  }
  *{box-sizing:border-box;margin:0;padding:0}
  html,body{width:1200px;height:1089px;overflow:hidden}
  body{background:var(--backdrop);font-family:"Asap Condensed",sans-serif;position:relative}

  .carton{position:absolute;top:170px;width:550px;height:760px;display:flex;box-shadow:0 20px 40px rgba(0,0,0,.18)}
  .carton--white{left:30px}
  .carton--black{left:620px}

  .panel{position:relative;height:100%}
  .panel--side{width:220px;padding:46px 20px 0}
  .panel--front{width:330px;text-align:center}

  .carton--white .panel--side{background:var(--white-side);color:var(--ink-dark)}
  .carton--white .panel--front{background:linear-gradient(180deg,var(--white-front),var(--white-front-low));color:var(--ink-dark)}
  .carton--black .panel--side{background:var(--black-side);color:var(--ink-light)}
  .carton--black .panel--front{background:var(--black-front);color:var(--ink-light)}

  .directions__title{font-size:14px;font-weight:700;letter-spacing:.3px;padding-bottom:3px;margin-bottom:12px;display:inline-block}
  .carton--white .directions__title{color:var(--accent-orange);border-bottom:3px solid var(--ink-dark)}
  .directions__text{font-size:12.5px;line-height:1.4;margin-bottom:16px}

  .badges{position:absolute;left:18px;bottom:30px;display:flex;gap:10px}
  .badge{width:34px;text-align:center;font-size:4px;line-height:1.2;text-transform:uppercase}
  .badge__ring{display:block;width:24px;height:24px;margin:0 auto 3px;border-radius:50%;border:1.5px solid currentColor}
  .carton--white .badge{color:var(--badge-orange)}
  .carton--black .badge{color:var(--badge-grey)}

  .brand{position:absolute;top:92px;left:0;right:0;display:flex;flex-direction:column;align-items:center;gap:10px}
  .brand__disc{width:70px;height:70px;border-radius:50%}
  .carton--white .brand__disc{background:var(--foil-green)}
  .carton--black .brand__disc{background:var(--foil-gold)}
  .brand__name{font-family:"Raleway",sans-serif;font-weight:600;font-size:18px;letter-spacing:2px;text-transform:uppercase}
  .carton--white .brand__name{color:var(--ink-dark)}
  .carton--black .brand__name{color:var(--foil-gold)}

  .title{position:absolute;top:270px;left:32px;right:32px;padding:8px 0 6px;border-top:3px solid;border-bottom:3px solid}
  .carton--white .title{color:var(--foil-green);border-color:var(--foil-green)}
  .carton--black .title{color:var(--foil-gold);border-color:var(--foil-gold)}
  .title__kicker{display:block;font-family:"Raleway",sans-serif;font-weight:500;font-size:18px;letter-spacing:4.5px}
  .title__line{display:block;font-family:"Raleway",sans-serif;font-weight:500;font-size:42px;line-height:1}
  .title__main{display:block;font-family:"Asap Condensed",sans-serif;font-weight:700;font-size:50px;line-height:1;letter-spacing:1px}
  .carton--white .title__main{color:var(--foil-green-deep)}

  .scent{position:absolute;top:505px;left:0;right:0;font-family:"Raleway",sans-serif;font-weight:500;font-size:22px}
  .claim{position:absolute;top:590px;left:0;right:0;font-family:"Raleway",sans-serif;font-size:12px;line-height:1.3}
  .claim__rule{width:190px;height:1.5px;margin:3px auto;background:var(--accent-orange)}
  .volume{position:absolute;bottom:40px;left:0;right:0;font-family:"Raleway",sans-serif;font-size:12px}
</style>
</head>
<body>

<section class="carton carton--white" aria-label="White box variant">
  <div class="panel panel--side">
    <h2 class="directions__title">DIRECTIONS</h2>
    <p class="directions__text">Squeeze 1-2 pulls of oil to the palm of your hand. for longer beards, use 3-4 pulls of oil. rub hands together and massage into beard .</p>
    <p class="directions__text">Finish by styling as usual with a beard comb or pick to spread beard oil evenly throughout your beard.</p>
    <p class="directions__text">Use daily for best results.</p>
    <div class="badges">
      <span class="badge"><span class="badge__ring"></span>Handcrafted</span>
      <span class="badge"><span class="badge__ring"></span>Cruelty free</span>
      <span class="badge"><span class="badge__ring"></span>Vegan</span>
      <span class="badge"><span class="badge__ring"></span>Sustainable</span>
    </div>
  </div>
  <div class="panel panel--front">
    <div class="brand"><span class="brand__disc"></span><span class="brand__name">Talon Meadows</span></div>
    <h1 class="title">
      <span class="title__kicker">HANDCRAFTED</span>
      <span class="title__line">PREMIUM</span>
      <span class="title__main">BEARD OIL</span>
    </h1>
    <p class="scent">Sweet Almond</p>
    <p class="claim">Made with 100% All-Natural<br>&amp; Organic Ingredients.<span class="claim__rule" style="display:block"></span>None of that artificial stuff!</p>
    <p class="volume">30ml / 1 fl. oz.</p>
  </div>
</section>

<section class="carton carton--black" aria-label="Black box variant">
  <div class="panel panel--side">
    <h2 class="directions__title">DIRECTIONS</h2>
    <p class="directions__text">Squeeze 1-2 pulls of oil to the palm of your hand. for longer beards, use 3-4 pulls of oil. rub hands together and massage into beard .</p>
    <p class="directions__text">Finish by styling as usual with a beard comb or pick to spread beard oil evenly throughout your beard.</p>
    <p class="directions__text">Use daily for best results.</p>
    <div class="badges">
      <span class="badge"><span class="badge__ring"></span>Handcrafted</span>
      <span class="badge"><span class="badge__ring"></span>Cruelty free</span>
      <span class="badge"><span class="badge__ring"></span>Vegan</span>
      <span class="badge"><span class="badge__ring"></span>Sustainable</span>
    </div>
  </div>
  <div class="panel panel--front">
    <div class="brand"><span class="brand__disc"></span><span class="brand__name">Talon Meadows</span></div>
    <h1 class="title">
      <span class="title__kicker">HANDCRAFTED</span>
      <span class="title__line">PREMIUM</span>
      <span class="title__main">BEARD OIL</span>
    </h1>
    <p class="scent">Sweet Almond</p>
    <p class="claim">Made with 100% All-Natural<br>&amp; Organic Ingredients.<span class="claim__rule" style="display:block"></span>None of that artificial stuff!</p>
    <p class="volume">30ml / 1 fl. oz.</p>
  </div>
</section>

</body>
</html>
```